Mezzanine Floor Manufacturer looking for a new business card design

We manufacture mezzanine floors and are providers of racking systems. We provide a range of items/services - simple rack repairs , full warehouse fit outs , manufacturer and install mezzanine floors , partitioning and large turnkey projects. Recently had a new website - www.corvane-shelving.co.uk and would like our business cards updating aswell . Our current card is single sided in the old logo colours (pdf attached) and needs updating.

Target Market(s)

We deal with large projects/ multi national companies and also smaller projects and companies throughout the UK ranging from a single warehouse to a large multi site company.

Industry/Entity Type

Business

Contact Information for Business Card

Will have job title,tel no's, email ,website address etc like example pdf

Requirements
Must have
• Hi - needs to use the colours of the logo & new website. Card needs to be professional

```html
<!DOCTYPE html>
<html lang="en">
<head>
<meta charset="utf-8">
<title>Corvane Business Card</title>
<link rel="stylesheet" href="https://fonts.googleapis.com/css2?family=Open+Sans:wght@400;600;700&display=swap">
<style>
  :root {
    --stage: #2e2e30;
    --card-white: #ffffff;
    --card-grey: #5e5e60;
    --brand-red: #d9272e;
    --ink-grey: #4f4f51;
    --text-light: #ffffff;
  }
  * { box-sizing: border-box; margin: 0; padding: 0; }
  html, body { width: 1200px; height: 900px; overflow: hidden; }
  body {
    background: var(--stage);
    font-family: "Open Sans", Arial, sans-serif;
    position: relative;
  }
  .card {
    position: absolute;
    width: 620px;
    height: 354px;
    border-radius: 22px;
    overflow: hidden;
    background: var(--card-white);
  }
  .card--services { left: 60px; top: 70px; }
  .card--contact { left: 520px; top: 470px; }

  .brand-mark {
    display: flex;
    align-items: center;
    gap: 12px;
    color: var(--brand-red);
    font-weight: 700;
    font-size: 50px;
    line-height: 1;
    white-space: nowrap;
  }
  .brand-mark__dot {
    width: 20px; height: 20px;
    border-radius: 50%;
    background: var(--brand-red);
  }

  /* Services side */
  .card--services .brand-mark {
    position: absolute; left: 50%; top: 56px; transform: translateX(-50%);
  }
  .services {
    position: absolute; left: 0; right: 0; top: 150px;
    text-align: center;
    text-transform: uppercase;
    color: var(--ink-grey);
    font-size: 15px;
    line-height: 21px;
    letter-spacing: 0.5px;
  }
  .services__heading { color: var(--brand-red); font-weight: 700; font-size: 16px; }
  .web-rule {
    position: absolute; left: 0; right: 0; top: 272px;
    display: flex; align-items: center; gap: 10px;
    padding: 0 22px;
    font-size: 15px; color: var(--ink-grey); letter-spacing: 1px;
  }
  .web-rule::before, .web-rule::after {
    content: ""; flex: 1; height: 1.5px; background: var(--brand-red);
  }
  .web-rule__domain { color: var(--brand-red); }

  /* Contact side */
  .contact-band {
    position: absolute; left: 0; right: 0; top: 172px; bottom: 0;
    background: var(--card-grey);
    border-top: 2px solid var(--brand-red);
  }
  .company-name {
    position: absolute; left: 0; right: 0; top: 38px;
    text-align: center;
    font-size: 48px; font-weight: 700; letter-spacing: 3px;
    color: var(--ink-grey);
  }
  .card--contact .brand-mark {
    position: absolute; left: 50%; top: 118px; transform: translateX(-50%);
    font-size: 36px;
  }
  .card--contact .brand-mark__dot { width: 16px; height: 16px; }
  .person {
    position: absolute; right: 330px; top: 196px;
    text-align: right; color: var(--text-light);
  }
  .person__name { font-size: 22px; font-weight: 700; letter-spacing: 1px; text-transform: uppercase; }
  .person__role { font-size: 13px; letter-spacing: 1px; text-transform: uppercase; margin-bottom: 6px; }
  .person__address { font-size: 15px; line-height: 21px; font-style: normal; }
  .contact-list {
    position: absolute; left: 318px; top: 198px;
    list-style: none; color: var(--text-light);
    font-size: 15px; line-height: 24px;
  }
  .contact-list li { display: flex; align-items: center; gap: 10px; }
  .contact-list svg { width: 13px; height: 13px; fill: var(--text-light); flex: none; }
</style>
</head>
<body>

<section class="card card--services">
  <div class="brand-mark"><span class="brand-mark__dot"></span>Corvane</div>
  <div class="services">
    <p class="services__heading">Services</p>
    <p>Rack repairs</p>
    <p>Full warehouse fit outs</p>
    <p>Manufacturer and install mezzanine floors</p>
    <p>Partitioning and large turnkey projects.</p>
  </div>
  <p class="web-rule"><span>www.<span class="web-rule__domain">corvane-shelving</span>.co.uk</span></p>
</section>

<section class="card card--contact">
  <h1 class="company-name">CORVANE</h1>
  <div class="contact-band"></div>
  <div class="brand-mark"><span class="brand-mark__dot"></span>Corvane</div>
  <div class="person">
    <p class="person__name">Daniel Hartley</p>
    <p class="person__role">Technical Sales</p>
    <address class="person__address">Forty mill close<br>Alder gate business Park<br>Belby, Derbyshire De9 4xQ</address>
  </div>
  <ul class="contact-list">
    <li><svg viewBox="0 0 16 16"><path d="M3 1l3 3-2 2c1 2 3 4 5 5l2-2 3 3-2 3C6 15 1 10 1 3z"/></svg>01632 960418</li>
    <li><svg viewBox="0 0 16 16"><path d="M4 0h8a1 1 0 0 1 1 1v14a1 1 0 0 1-1 1H4a1 1 0 0 1-1-1V1a1 1 0 0 1 1-1zm1 2v10h6V2z"/></svg>07700 900274</li>
    <li><svg viewBox="0 0 16 16"><path d="M1 5h14v8H1zM4 1h8v4H4zm0 9h8v3H4z"/></svg>01632 960519</li>
    <li><svg viewBox="0 0 16 16"><path d="M1 3h14v10H1zm1 1v1l6 4 6-4V4z"/></svg>daniel@corvane-shelving.co.uk</li>
    <li><svg viewBox="0 0 16 16"><path d="M8 1a7 7 0 1 0 0 14A7 7 0 0 0 8 1zm-5 7h10M8 2c2 2 2 10 0 12M8 2c-2 2-2 10 0 12" stroke="#fff" stroke-width="1" fill="none"/></svg>www.corvane-shelving.co.uk</li>
  </ul>
</section>

</body>
</html>
```